Flyer für Photovoltaikanlagen
Zielgruppe
Aufbau bzw. unterteilung, stelle ich mir vor das es wie auf 0124_pv_aquise_a4_lws.pdf ausgelegt.
FesterBestandteile:
- Abreißkarte wie auf Flyer 1:1
- Produktfotos + Logo ( Modul KE-Lumin, QVR Batterie, Helvorn - Wechselrichter ) am besten über die Abreißkarte
- Schönes Fotos mit Dachanlage ( wenn möglich dunkele Module / Full Black Module)
- Rechnen Bsp. zur Unabhängigkeit, wie auf dem anghängten Angebot.( Seite 2 )
Inhalte die eingbaut werden sollten, wenn möglich:
Wir bauen Photovoltaikanlagen und sind Dachdeckermeisterbetrieben und Elektromeisterbetrieb (evtl. auch als Logos)
Photovoltaikanlagen Neubau / Erweiterung
- Bedarfgerechte Beratung inkl. Besichtung der Immobilie
- Transparentes Angebot
- Netzanfrage
- Markstammdatenregisterung (Vergütung für verkaufen Strom)
- Planung & Auslegung (internes Ingeneurbüro)
- Montage Dach(Dachdeckermeisterbetrieb)
- Monate Elektro inkl. Zähersetzung (Elektromeisterbetrieb)
- Einweisung ins Monitoring (App)
After Sales Service
- Service & Wartung
- Reinigung
Modern
Bedarfweckend
Produktfotos verwenden

```html
<!DOCTYPE html>
<html lang="de">
<head>
<meta charset="utf-8">
<title>Solvera – Photovoltaik Flyer</title>
<link href="https://fonts.googleapis.com/css2?family=Bebas+Neue&family=Poppins:wght@400;500;600;700;800&display=swap" rel="stylesheet">
<style>
:root{
  --yellow:#f4c955;
  --navy:#3b5170;
  --navy-dark:#2f4361;
  --blue-light:#6f8db5;
  --grey-row:#e8e9e9;
  --text:#4a4f57;
  --white:#ffffff;
  --backdrop:#b6b6b6;
}
*{margin:0;padding:0;box-sizing:border-box}
html,body{width:1200px;height:1117px;overflow:hidden;background:var(--backdrop)}
body{position:relative;font-family:"Poppins",sans-serif}
.page{position:absolute;top:174px;width:545px;height:769px;overflow:hidden;background:var(--white)}
.page--front{left:46px}
.page--back{left:609px}
.page-bg{position:absolute;inset:0}
.abs{position:absolute}
.brand{position:absolute;left:44px;top:34px;display:flex;align-items:center;gap:6px}
.brand__dot{width:14px;height:14px;border-radius:50%;background:var(--yellow)}
.brand__name{font-family:"Poppins",sans-serif;font-weight:800;font-size:22px;color:var(--white);letter-spacing:1px}
.headline{font-family:"Bebas Neue",sans-serif;color:var(--white);line-height:.92}
.headline--yellow{color:var(--yellow)}
.front-title{left:40px;top:146px;font-size:50px}
.front-sub{left:40px;top:240px;font-size:35px}
.front-intro{left:40px;top:305px;width:258px;font-size:9.2px;font-weight:600;line-height:12.1px;color:var(--white)}
.module-photo{left:312px;top:319px;width:233px;height:428px;background:linear-gradient(180deg,#2b2c2e,#1f2022);border:2px solid #3d3e40}
.section-arrow{left:0;top:413px}
.section-title{left:40px;top:428px;font-family:"Bebas Neue",sans-serif;font-size:36px;color:var(--navy);line-height:1}
.spec-table{left:28px;top:468px;width:265px;border-collapse:separate;border-spacing:2px 0;font-size:9px;font-weight:600;color:var(--text)}
.spec-table td{height:26px;padding-left:10px}
.spec-table td:first-child{width:110px}
.spec-table tr:nth-child(odd) td{background:var(--grey-row)}
.contact-band{left:0;top:673px;width:545px;height:96px;background:var(--yellow);border-top:3px solid var(--navy)}
.contact-band__ask{position:absolute;left:40px;top:12px;font-size:18px;font-weight:700;color:var(--navy)}
.contact-band__call{position:absolute;left:40px;top:34px;font-size:15px;font-weight:500;color:var(--navy)}
.contact-band__phone{position:absolute;left:40px;top:50px;display:flex;align-items:center;gap:6px;font-size:27px;font-weight:700;color:var(--navy)}
.back-title{left:37px;top:148px;font-size:39px;line-height:.9}
.service-list{left:322px;top:57px;width:215px;list-style:none;font-size:9px;font-weight:700;color:var(--white);line-height:11.5px}
.service-list li{display:flex;gap:9px;margin-bottom:11.5px}
.service-list li svg{flex:none;margin-top:1px}
.why-title{left:38px;top:372px;font-family:"Bebas Neue",sans-serif;font-size:26px;color:var(--navy);white-space:nowrap}
.col-left{left:40px;top:400px;width:256px}
.col-left h3{font-size:10.5px;font-weight:700;color:var(--navy);line-height:13px;margin-bottom:20px}
.col-left p{font-size:8.9px;line-height:11.6px;color:var(--text);margin-bottom:11.6px}
.col-divider{left:309px;top:402px;width:1px;height:310px;background:#cfd3d8}
.col-right{left:322px;top:398px;width:200px}
.col-right h3{font-size:10.5px;font-weight:700;color:var(--navy);line-height:13px;margin-bottom:8px}
.col-right h3 span{border-bottom:2px solid var(--yellow)}
.step{display:flex;gap:9px;margin-bottom:14px}
.step svg{flex:none;margin-top:3px}
.step h4{font-size:11px;font-weight:700;color:var(--navy);line-height:14px;margin-bottom:3px}
.step p{font-size:8.6px;font-weight:700;color:var(--text);line-height:11px}
.footer-band{left:0;top:722px;width:545px;height:47px;background:var(--yellow);border-top:3px solid var(--navy);display:flex;align-items:center;justify-content:center;gap:16px;font-size:11px;font-weight:700;color:var(--navy)}
.footer-band span{display:flex;align-items:center;gap:5px}
</style>
</head>
<body>

<!-- Vorderseite -->
<section class="page page--front">
  <svg class="page-bg" viewBox="0 0 545 769" width="545" height="769" aria-hidden="true">
    <defs>
      <linearGradient id="roofGrad" x1="0" y1="0" x2="1" y2="1">
        <stop offset="0" stop-color="#f6f1e6"/>
        <stop offset=".45" stop-color="#b7c2d3"/>
        <stop offset="1" stop-color="#3e5577"/>
      </linearGradient>
    </defs>
    <rect width="545" height="769" fill="var(--yellow)"/>
    <rect y="300" width="545" height="373" fill="var(--white)"/>
    <path d="M0 28 C110 75 260 80 380 50 C460 30 515 30 545 40 L545 318 L312 318 L312 386 C220 396 110 410 0 408 Z" fill="var(--yellow)"/>
    <path d="M0 28 C110 75 260 80 380 50 C460 30 515 30 545 40 L545 318 L312 318 L312 377 C220 386 110 400 0 398 Z" fill="var(--navy)"/>
    <path d="M0 15 C110 62 260 68 380 40 C460 20 515 18 545 22 L545 40 C515 30 460 30 380 50 C260 80 110 75 0 28 Z" fill="var(--blue-light)"/>
    <path role="img" aria-label="Foto: Monteur mit Helm montiert Solarmodule auf einem Dach" d="M160 68 C260 52 400 30 545 46 L545 318 L330 318 C260 300 220 260 195 200 C180 150 168 110 160 68 Z" fill="url(#roofGrad)" opacity=".9"/>
  </svg>

  <div class="brand"><span class="brand__dot"></span><span class="brand__name">SOLVERA</span></div>

  <h1 class="abs headline front-title">Photovoltaik<br>Anlagen Neubau</h1>
  <h2 class="abs headline headline--yellow front-sub">Solaranlagen vom<br>Niederrhein</h2>
  <p class="abs front-intro">Wir von der Solvera GmbH sind Marktführer, wenn es um die Rundum-Betreuung im Bereich von Photovoltaikanlagen, Photovoltaik Wartung und die Installation von Solaranlagen geht. Mit Sitz am Niederrhein in Musterstadt sind wir Ansprechpartner Nummer 1 in ganz NRW für die neueste Solaranlagen-Technik.</p>

  <div class="abs module-photo" role="img" aria-label="Produktfoto: schwarzes Full-Black-Solarmodul"></div>

  <svg class="abs section-arrow" width="31" height="61" viewBox="0 0 31 61" aria-hidden="true"><path d="M0 0 L31 30.5 L0 61 Z" fill="var(--yellow)"/></svg>
  <h2 class="abs section-title">Solarmodule</h2>

  <table class="abs spec-table">
    <tr><td>Hersteller</td><td>KE-Lumin</td></tr>
    <tr><td>Type</td><td>KLM54-435/FB</td></tr>
    <tr><td>Leistung</td><td>435 Wp</td></tr>
    <tr><td>Wirkungsgrad</td><td>21,8 %</td></tr>
    <tr><td>Herstellergarantie</td><td>25 Jahre</td></tr>
    <tr><td>Leistungsgarantie</td><td>30 Jahre / 87.40%</td></tr>
    <tr><td>Zelltyp</td><td>monokristalline Halbzellen</td></tr>
  </table>

  <div class="abs contact-band">
    <p class="contact-band__ask">BERATUNG GEWÜNSCHT?</p>
    <p class="contact-band__call">Rufen Sie uns an:</p>
    <p class="contact-band__phone">
      <svg width="22" height="24" viewBox="0 0 24 24" aria-hidden="true"><path d="M6.6 10.8a15.2 15.2 0 0 0 6.6 6.6l2.2-2.2a1 1 0 0 1 1-.25 11.4 11.4 0 0 0 3.6.57 1 1 0 0 1 1 1V20a1 1 0 0 1-1 1A17 17 0 0 1 3 4a1 1 0 0 1 1-1h3.5a1 1 0 0 1 1 1c0 1.25.2 2.45.57 3.57a1 1 0 0 1-.25 1z" fill="var(--navy)"/></svg>
      0201 5550190
    </p>
  </div>
</section>

<!-- Rückseite -->
<section class="page page--back">
  <svg class="page-bg" viewBox="0 0 545 769" width="545" height="769" aria-hidden="true">
    <defs>
      <linearGradient id="panelGrad" x1="0" y1="0" x2="1" y2="1">
        <stop offset="0" stop-color="#0d1220"/>
        <stop offset=".55" stop-color="#2c4a86"/>
        <stop offset="1" stop-color="#8ea6cf"/>
      </linearGradient>
    </defs>
    <rect width="545" height="769" fill="var(--white)"/>
    <rect width="545" height="60" fill="var(--yellow)"/>
    <path d="M0 28 C110 75 260 80 380 50 C460 30 515 30 545 40 L545 338 C470 360 380 370 300 366 C180 362 80 355 0 360 Z" fill="var(--yellow)"/>
    <path d="M0 28 C110 75 260 80 380 50 C460 30 515 30 545 40 L545 330 C470 352 380 360 300 356 C180 350 80 342 0 350 Z" fill="var(--navy)"/>
    <path d="M0 15 C110 62 260 68 380 40 C460 20 515 18 545 22 L545 40 C515 30 460 30 380 50 C260 80 110 75 0 28 Z" fill="var(--blue-light)"/>
    <path role="img" aria-label="Foto: dunkle Solarmodule auf einem Dach im Gegenlicht" d="M0 40 C110 75 220 80 305 66 L305 330 C200 320 120 310 0 326 Z" fill="url(#panelGrad)"/>
  </svg>

  <div class="brand"><span class="brand__dot"></span><span class="brand__name">SOLVERA</span></div>

  <h1 class="abs headline back-title">Bedarfgerechte<br>Beratung inkl.<br>Besichtung der<br><span class="headline--yellow">Immobilie</span></h1>

  <ul class="abs service-list">
    <li><svg width="10" height="10" viewBox="0 0 10 10"><circle cx="5" cy="5" r="5" fill="var(--yellow)"/><path d="M2.8 5.2l1.5 1.4 2.9-3" stroke="var(--navy)" stroke-width="1.3" fill="none"/></svg>Transparentes Angebot</li>
    <li><svg width="10" height="10" viewBox="0 0 10 10"><circle cx="5" cy="5" r="5" fill="var(--yellow)"/><path d="M2.8 5.2l1.5 1.4 2.9-3" stroke="var(--navy)" stroke-width="1.3" fill="none"/></svg>Netzanfrage</li>
    <li><svg width="10" height="10" viewBox="0 0 10 10"><circle cx="5" cy="5" r="5" fill="var(--yellow)"/><path d="M2.8 5.2l1.5 1.4 2.9-3" stroke="var(--navy)" stroke-width="1.3" fill="none"/></svg><span>Markstammdatenregisterung<br>(Vergütung für verkaufen Strom)</span></li>
    <li><svg width="10" height="10" viewBox="0 0 10 10"><circle cx="5" cy="5" r="5" fill="var(--yellow)"/><path d="M2.8 5.2l1.5 1.4 2.9-3" stroke="var(--navy)" stroke-width="1.3" fill="none"/></svg><span>Planung &amp; Auslegung<br>(internes Ingeneurbüro)</span></li>
    <li><svg width="10" height="10" viewBox="0 0 10 10"><circle cx="5" cy="5" r="5" fill="var(--yellow)"/><path d="M2.8 5.2l1.5 1.4 2.9-3" stroke="var(--navy)" stroke-width="1.3" fill="none"/></svg><span>Montage Dach<br>(Dachdeckermeisterbetrieb)</span></li>
    <li><svg width="10" height="10" viewBox="0 0 10 10"><circle cx="5" cy="5" r="5" fill="var(--yellow)"/><path d="M2.8 5.2l1.5 1.4 2.9-3" stroke="var(--navy)" stroke-width="1.3" fill="none"/></svg><span>Monate Elektro inkl. Zähersetzung<br>(Elektromeisterbetrieb)</span></li>
    <li><svg width="10" height="10" viewBox="0 0 10 10"><circle cx="5" cy="5" r="5" fill="var(--yellow)"/><path d="M2.8 5.2l1.5 1.4 2.9-3" stroke="var(--navy)" stroke-width="1.3" fill="none"/></svg>Einweisung ins Monitoring (App)</li>
    <li><svg width="10" height="10" viewBox="0 0 10 10"><circle cx="5" cy="5" r="5" fill="var(--yellow)"/><path d="M2.8 5.2l1.5 1.4 2.9-3" stroke="var(--navy)" stroke-width="1.3" fill="none"/></svg>After Sales Service</li>
    <li><svg width="10" height="10" viewBox="0 0 10 10"><circle cx="5" cy="5" r="5" fill="var(--yellow)"/><path d="M2.8 5.2l1.5 1.4 2.9-3" stroke="var(--navy)" stroke-width="1.3" fill="none"/></svg>Service &amp; Wartung</li>
    <li><svg width="10" height="10" viewBox="0 0 10 10"><circle cx="5" cy="5" r="5" fill="var(--yellow)"/><path d="M2.8 5.2l1.5 1.4 2.9-3" stroke="var(--navy)" stroke-width="1.3" fill="none"/></svg>Reinigung</li>
  </ul>

  <h2 class="abs why-title">Warum Sie sich jetzt eine Solaranlage zulegen sollten</h2>

  <div class="abs col-left">
    <h3>Photovoltaik-Förderung 2024:<br>Das müssen Hausbesitzer jetzt wissen…</h3>
    <p>Mit dem Beschluss der Schuldenbremse werden 2024 zahlreiche Förderprogramme gestrichen. Vor allem Ausgaben aus dem Klima- und Transformationsfonds werden geringer ausfallen. Dazu gehört auch die aktuelle Solarförderung, die laut Berger gekürzt werden könnte. Experten raten: Die Anschaff ung lohnt sich jetzt, solange Sie von der „steuerfreien“ Anlage profi tieren können.</p>
    <p>Bundesweite Förderung: Günstiger denn je<br>Für Hausbesitzer ist es gerade so attraktiv wie noch nie, in eine eigene Solaranlage zu investieren. In Deutschland wurden seit Januar 2023 einige Förderprogramme und Steuererleichterungen für private Solaranlagen festgelegt. Die Höhe und Bedingungen der Förderung ist von verschiedenen Faktoren abhängig. Dazu gehören Größe der Solaranlage, Stromverbrauch und Anbieter. Durch Steuererleichterungen müssen Hausbesitzer momentan für eine Photovoltaikanlage keine Mehrwertsteuer, Einkommensteuer und Gewerbesteuer zahlen.</p>
    <p>Die Investition lohnt sich jetzt mehr denn je.</p>
  </div>

  <div class="abs col-divider"></div>

  <div class="abs col-right">
    <h3>In vier Schritten zur <span>eigenen</span><br>Solaranlage</h3>
    <div class="step">
      <svg width="10" height="10" viewBox="0 0 10 10"><circle cx="5" cy="5" r="5" fill="var(--yellow)"/><path d="M2.8 5.2l1.5 1.4 2.9-3" stroke="var(--white)" stroke-width="1.3" fill="none"/></svg>
      <div><h4>Beratung</h4><p>Wir beraten Sie umfassend über geeignete Solaranlagen-Produkte. Vereinbaren Sie am besten gleich Ihren vor-Ort-Termin</p></div>
    </div>
    <div class="step">
      <svg width="10" height="10" viewBox="0 0 10 10"><circle cx="5" cy="5" r="5" fill="var(--yellow)"/><path d="M2.8 5.2l1.5 1.4 2.9-3" stroke="var(--white)" stroke-width="1.3" fill="none"/></svg>
      <div><h4>Fördermöglichkeiten</h4><p>Sie müssen sich nicht selbst um geeignete Fördermöglichkeiten kümmern. Dazu erhalten Sie eine detaillierte Beratung.</p></div>
    </div>
    <div class="step">
      <svg width="10" height="10" viewBox="0 0 10 10"><circle cx="5" cy="5" r="5" fill="var(--yellow)"/><path d="M2.8 5.2l1.5 1.4 2.9-3" stroke="var(--white)" stroke-width="1.3" fill="none"/></svg>
      <div><h4>Planung &amp; Installation</h4><p>Sie müssen sich nicht selbst um geeignete Fördermöglichkeiten kümmern. Dazu erhalten Sie eine detaillierte Beratung.</p></div>
    </div>
    <div class="step">
      <svg width="10" height="10" viewBox="0 0 10 10"><circle cx="5" cy="5" r="5" fill="var(--yellow)"/><path d="M2.8 5.2l1.5 1.4 2.9-3" stroke="var(--white)" stroke-width="1.3" fill="none"/></svg>
      <div><h4>Inbetriebnahme &amp; Monitoring</h4><p>Genießen Sie den Ertrag Ihrer neuen Solaranlage. Wir übernehmen die Fernwartung nach Inbetriebnahme.</p></div>
    </div>
  </div>

  <div class="abs footer-band">
    <span><svg width="10" height="11" viewBox="0 0 24 24" aria-hidden="true"><path d="M12 2a7 7 0 0 0-7 7c0 5.2 7 13 7 13s7-7.8 7-13a7 7 0 0 0-7-7zm0 9.5A2.5 2.5 0 1 1 12 6.5a2.5 2.5 0 0 1 0 5z" fill="var(--navy)"/></svg>Lindenweg 8 · 46500 Musterstadt</span>
    <span><svg width="11" height="11" viewBox="0 0 24 24" aria-hidden="true"><circle cx="12" cy="12" r="11" fill="var(--navy)"/><path d="M9 7.5l1.6 2.6-1 1.2a7 7 0 0 0 3.1 3.1l1.2-1 2.6 1.6-.8 1.8c-4.3-.2-7.6-3.5-7.8-7.8z" fill="var(--yellow)"/></svg>0 20 1 / 55 50 20</span>
    <span><svg width="11" height="11" viewBox="0 0 24 24" aria-hidden="true"><circle cx="12" cy="12" r="10" fill="none" stroke="var(--navy)" stroke-width="2"/><path d="M2 12h20M12 2c3 3 3 17 0 20M12 2c-3 3-3 17 0 20" fill="none" stroke="var(--navy)" stroke-width="1.6"/></svg>solvera-service.example</span>
  </div>
</section>

</body>
</html>
```